Tidy Haven Path half fold brochure design

I need a brochure for a new company. The name of the company is Tidy Haven Path. I am a Professional Organizer. I am requesting a one fold brochure 11" wide x 8.5" high (obviously once folded 5.5" wide x 8.5" high) brochure. I have been told this may need to be designed as a flyer? I have attached a VERY BASIC layout of what I think I am looking for. I have also attached the original logos in all the different formats I have. I would like to have a very light green background & the text I have in orange please make orange. PLEASE feel free to add color to my "Tidy Haven Path" logo's and use light/soft green & orange shades if possible (OK to go darker for BOLD purposes) The brochure DOES NOT have to stick to this layout, again just what I THINK I want :) - THANK YOU

EDIT: 01-21-15 Remove MARLENE KUDSIK from all 3 places (front, bottom inside right & back) Remove just the KUDSIK from the 1st line on the back. PRIVACY & ETHICS on the back, please remove "PRIVACY &", leave Ethics and the 1st line of the text under it. Please remove all of the text following the 1st sentence. THANK YOU

Industry/Entity Type

It Company

```html
<!DOCTYPE html>
<html lang="en">
<head>
<meta charset="utf-8">
<title>Tidy Haven Path – Brochure Inside Spread</title>
<link rel="stylesheet" href="https://fonts.googleapis.com/css2?family=Roboto+Condensed:wght@700&family=Arimo:ital,wght@0,400;0,700;1,400&display=swap">
<style>
  :root {
    --backdrop: #2e3237;
    --page: #eefaea;
    --ink: #1e1e1e;
    --green: #1ba34b;
    --blue: #1a4f9c;
    --label: #f2f2f2;
  }
  * { box-sizing: border-box; margin: 0; padding: 0; }
  html, body { width: 1200px; height: 912px; overflow: hidden; }
  body {
    background: var(--backdrop);
    font-family: "Arimo", Arial, sans-serif;
    color: var(--ink);
    position: relative;
  }
  .panel-label {
    position: absolute; top: 15px;
    font: 700 12px "Arimo", Arial, sans-serif;
    color: var(--label);
    text-align: center;
  }
  .panel {
    position: absolute; top: 38px; height: 834px;
    background: var(--page);
  }
  .panel-left { left: 55px; width: 538px; padding: 50px 48px 0 49px; }
  .panel-right { left: 605px; width: 542px; padding: 54px 50px 0 50px; }
  .lead, .question, .section, .closing {
    font-family: "Roboto Condensed", "Arial Narrow", sans-serif;
    font-weight: 700;
    color: var(--green);
  }
  .lead {
    font-size: 17px; line-height: 21px;
    text-align: center; padding: 0 18px; margin-bottom: 12px;
  }
  .question { font-size: 14px; line-height: 18px; margin: 4px 0 3px; }
  .copy {
    font-size: 15.4px; line-height: 22.7px;
    text-align: justify; margin-bottom: 4px;
  }
  .closing {
    font-size: 17px; line-height: 21px;
    text-align: center; margin-top: 40px;
  }
  .section { font-size: 14px; line-height: 18px; margin: 8px 0 5px; }
  .source { color: var(--blue); font-style: italic; }
  .services { list-style: none; }
  .services li {
    display: flex; align-items: center; gap: 12px;
    font-size: 15.4px; line-height: 27.5px; padding-left: 1px;
  }
  .tick { width: 12px; height: 12px; flex: none; }
  .panel-right .closing { margin-top: 37px; }
</style>
</head>
<body>
  <div class="panel-label" style="left:55px;width:538px;">INSIDE-1</div>
  <div class="panel-label" style="left:605px;width:542px;">INSIDE-2</div>

  <section class="panel panel-left">
    <h2 class="lead">Getting organized isn't all about everything being in its proper place. It can also require overcoming fears and anxieties such as:</h2>

    <h3 class="question">“How do I start?”</h3>
    <p class="copy">You begin by getting help from a professional organizer. No one can do everything; everyone needs a helping hand at times. (I bring my vehicle to a mechanic when it needs service, even for just a simple oil change!)</p>

    <h3 class="question">“Am I going to have to get rid of ALL my things?”</h3>
    <p class="copy">Definitely not! There is a process that will help you decide what to keep and what you would be willing to part with. (I can help you determine the practical and monetary worth of something. Only you can determine its personal value.)</p>

    <h3 class="question">“I don't have time”</h3>
    <p class="copy">Now you will! Getting organized will actually save you time. You will know where your belongings are, find them quickly and avoid the time it takes to run out and purchase a new one. (You will have actually created more time to enjoy the lifestyle that is important to you.)</p>

    <p class="copy" style="margin-top:6px;">We all have anxiety about something that prevents or inhibits us from taking action toward a solution. Whether you want someone to take over the project or a helping hand (nudge) is all you really need, a professional organizer is the perfect way to get started. Getting organized is going to be a process of progress, not perfection. It will require some level of support and continued work on you part, but the rewards will far outweigh the efforts.</p>

    <p class="closing">TOGETHER WE CAN CONQUER THE CLUTTER AND CREATE CLARITY</p>
  </section>

  <section class="panel panel-right">
    <h3 class="section" style="margin-top:0;">What is a professional organizer?</h3>
    <p class="copy">“A Professional Organizer enhances the lives of clients by designing systems and processes using organizing principles and through transferring organizing skills. Professional Organizers help individuals and businesses take control of their surroundings, their time, their paper, and their systems for life.” <span class="source">Guild of Home Organizing Professionals.</span></p>
    <p class="copy" style="margin-top:6px;">Whether you are too busy, too confused, over whelmed, tired, stressed or just don't know where to start, I offer a variety of hands on services to help you bring a sense of fun, freedom and functionality to almost any space.</p>

    <svg width="0" height="0" style="position:absolute">
      <symbol id="tick-box" viewBox="0 0 12 12">
        <rect x="0.6" y="0.6" width="10.8" height="10.8" fill="none" stroke="#1ba34b" stroke-width="1.2"/>
        <path d="M2.6 6.2 L5 8.6 L10 2.8" fill="none" stroke="#1ba34b" stroke-width="1.6"/>
      </symbol>
    </svg>

    <h3 class="section">ATTIC TO BASEMENT:</h3>
    <ul class="services">
      <li><svg class="tick"><use href="#tick-box"/></svg>Sorting - Purging - Organizing</li>
    </ul>
    <h3 class="section">PAPER CONTROL:</h3>
    <ul class="services">
      <li><svg class="tick"><use href="#tick-box"/></svg>Sorting - Purging - Organizing</li>
      <li><svg class="tick"><use href="#tick-box"/></svg>Household, home office &amp; home based filing systems</li>
    </ul>
    <h3 class="section">DOWNSIZING:</h3>
    <ul class="services">
      <li><svg class="tick"><use href="#tick-box"/></svg>Sorting - Purging - Organizing - Labeling</li>
      <li><svg class="tick"><use href="#tick-box"/></svg>Packing &amp; unpacking</li>
    </ul>
    <h3 class="section">REMOVAL:</h3>
    <ul class="services">
      <li><svg class="tick"><use href="#tick-box"/></svg>Light trash &amp; proper disposal</li>
      <li><svg class="tick"><use href="#tick-box"/></svg>Donations &amp; light recyclables to proper locations</li>
      <li><svg class="tick"><use href="#tick-box"/></svg>Shredding Service</li>
    </ul>
    <h3 class="section">FOLLOW UP:</h3>
    <ul class="services">
      <li><svg class="tick"><use href="#tick-box"/></svg>Routine “clutter maintenance” visits</li>
    </ul>

    <p class="closing">For projects not listed above, please contact me.</p>
  </section>
</body>
</html>
```